Building company needs a letterhead design

I'm after a modern but professional letter head.
Must have the below details:
- Logo
- Website - TARVELGROUP.COM.AU
- Email - INFO@TARVELGROUP.COM.AU
- Office - 03 58206317
- Mobile number - 0413865290
- ABN - 47 318 264 105
...........................................................................................................................................................................................................................
- Logo
- Office - 03 58206317
- ABN - 47 318 264 105

Target Market(s)

.

Industry/Entity Type

Construction Company

Font styles to use
Sans Serif

Requirements
Must have
• Must have the below details:
• - Logo
• - Website - TARVELGROUP.COM.AU
• - Email - INFO@TARVELGROUP.COM.AU
• - Office - 03 58206317
• - Mobile number - 0413865290
• - ABN - 47 318 264 105
Nice to have
• .
Should not have
• .

```html
<!DOCTYPE html>
<html lang="en">
<head>
<meta charset="utf-8">
<title>Tarvel Building Group – Letterhead</title>
<link rel="stylesheet" href="https://fonts.googleapis.com/css2?family=Arimo:wght@400;700&display=swap">
<style>
  :root {
    --slate: #6d6e71;
    --amber: #fdb813;
    --ink: #6d6e71;
    --paper: #ffffff;
  }
  * { margin: 0; padding: 0; box-sizing: border-box; }
  html, body { width: 927px; height: 1200px; overflow: hidden; background: var(--paper); }
  .letterhead {
    position: relative;
    width: 927px;
    height: 1200px;
    background: var(--paper);
    font-family: "Arimo", Arial, sans-serif;
    overflow: hidden;
  }
  .band { position: absolute; width: 74px; }
  .band--slate { left: 41px; background: var(--slate); }
  .band--amber { left: 121px; background: var(--amber); }
  .band--top { top: 0; height: 69px; }
  .band--long { top: 217px; height: 983px; }

  .brand {
    position: absolute;
    left: 41px;
    top: 82px;
    width: 154px;
    text-align: center;
    color: var(--amber);
    font-weight: 700;
  }
  .brand__mark {
    display: block;
    width: 44px;
    height: 44px;
    margin: 0 auto 10px;
    background: var(--amber);
  }
  .brand__name { display: block; font-size: 26px; letter-spacing: 1px; line-height: 1; }
  .brand__tag { display: block; font-size: 10.5px; letter-spacing: 1.2px; margin-top: 4px; }

  .contact {
    position: absolute;
    right: 51px;
    top: 69px;
    list-style: none;
    text-align: right;
    color: var(--ink);
    font-size: 13.5px;
    line-height: 17.5px;
  }
  .contact li { display: flex; justify-content: flex-end; align-items: center; gap: 4px; }
  .contact svg { width: 11px; height: 11px; flex: none; }
  .contact .gap { margin-left: 8px; }
  .contact .label { color: var(--amber); }

  .tab { position: absolute; left: 896px; width: 31px; }
  .tab--amber { top: 73px; height: 31px; background: var(--amber); }
  .tab--slate { top: 107px; height: 30px; background: var(--slate); }
</style>
</head>
<body>
<main class="letterhead">
  <div class="band band--slate band--top"></div>
  <div class="band band--amber band--top"></div>

  <div class="brand">
    <span class="brand__mark"></span>
    <span class="brand__name">TARVEL</span>
    <span class="brand__tag">BUILDING GROUP</span>
  </div>

  <div class="band band--slate band--long"></div>
  <div class="band band--amber band--long"></div>

  <ul class="contact">
    <li>www.tarvelgroup.com.au
      <svg viewBox="0 0 12 12"><circle cx="6" cy="6" r="4.5" fill="none" stroke="#fdb813" stroke-width="1.2"/><path d="M1.5 6h9M6 1.5c-2 2.5-2 6.5 0 9M6 1.5c2 2.5 2 6.5 0 9" fill="none" stroke="#fdb813" stroke-width="0.9"/></svg>
    </li>
    <li>info@tarvelgroup.com.au
      <svg viewBox="0 0 12 12"><rect x="1" y="2.5" width="10" height="7" fill="none" stroke="#fdb813" stroke-width="1.1"/><path d="M1 2.5l5 4 5-4" fill="none" stroke="#fdb813" stroke-width="1.1"/></svg>
    </li>
    <li>03 58206317
      <svg viewBox="0 0 12 12"><path d="M3 1.5l1.8 2.2-1 1.3c.7 1.5 1.7 2.5 3.2 3.2l1.3-1L10.5 9 9 10.5C5 10 2 7 1.5 3z" fill="#fdb813"/></svg>
      <span class="gap">0413865290</span>
      <svg viewBox="0 0 12 12"><path d="M2 1.5l2 2.5-1 1.2c.8 1.6 2 2.8 3.6 3.6l1.2-1L10.5 10 9.5 11C5 10.5 1.5 7 1 2.5z" fill="none" stroke="#fdb813" stroke-width="1.1"/></svg>
    </li>
    <li>47 318 264 105 - <span class="label">ABN</span></li>
  </ul>

  <div class="tab tab--amber"></div>
  <div class="tab tab--slate"></div>
</main>
</body>
</html>
```